Web Design for Harbor Ledger Allies

Harbor Ledger Allies needs the photoshop files for a simple, clean and professional website design. The company is building a network of bookkeepers/accountants to handle outsourced bookkeeping services for start ups and small businesses. It needs to both attract bookkeepers to become partners and give clients confidence in the professional network. The partners will use products like Tallymint Web, Brightfolio.example and PennyTrim.example for start ups, as well as help with tasks using the clients existing accounting software.

A home and subpage design is needed. I'll award the work based on the home design. The minor subpage changes can be worked out in the workroom stage.

The pages for the navigation will be: Home, Services, Locations, Partners, FAQ, Contact

```html
<!DOCTYPE html>
<html lang="en">
<head>
<meta charset="utf-8">
<title>Harbor Ledger Allies</title>
<link href="https://fonts.googleapis.com/css2?family=Open+Sans:wght@300;400;600&display=swap" rel="stylesheet">
<style>
:root{
  --brand:#009ddd;
  --slate:#5e5f61;
  --ink:#3a3a3a;
  --muted:#d0d0d0;
  --footer:#d2d2d2;
  --white:#ffffff;
}
*{margin:0;padding:0;box-sizing:border-box}
html,body{width:960px;height:1200px;overflow:hidden}
body{font-family:"Open Sans",Arial,sans-serif;background:var(--white);color:var(--ink)}
.site-header{position:absolute;top:0;left:0;width:960px;height:79px;background:var(--brand)}
.brand{position:absolute;left:58px;top:17px;display:flex;align-items:center;gap:10px;color:var(--white)}
.brand-mark{width:40px;height:40px;border:3px solid var(--white);border-radius:4px}
.brand-name{font-size:14px;font-weight:600;line-height:14px;text-transform:uppercase;letter-spacing:.3px}
.main-nav{position:absolute;top:46px;left:409px;display:flex;gap:0}
.main-nav a{color:var(--white);text-decoration:none;font-size:11.5px;text-transform:uppercase;margin-right:40px}
.hero{position:absolute;top:79px;left:0;width:960px;height:358px;background:linear-gradient(135deg,#dfe9ef 0%,#b9c9d6 35%,#eef3f6 60%,#8fa6bf 100%)}
.why{position:absolute;top:437px;left:0;width:960px;height:245px;background:var(--slate);text-align:center;color:var(--white)}
.why h1{font-weight:300;font-size:40px;margin-top:38px;letter-spacing:.3px}
.why p{width:590px;margin:18px auto 0;font-size:12px;line-height:13.5px;color:var(--muted)}
.btn{display:inline-block;margin-top:27px;width:129px;height:35px;line-height:35px;background:var(--brand);color:var(--white);font-size:12px;text-decoration:none;border-radius:3px}
.services{position:absolute;top:682px;left:0;width:960px;height:260px}
.service{position:absolute;top:48px;width:230px}
.service-icon{width:68px;height:68px;background:var(--brand);border-radius:5px;margin:0 auto;display:flex;align-items:center;justify-content:center}
.service h2{font-weight:400;font-size:16px;text-align:center;margin-top:12px;color:#444}
.service p{font-size:10.5px;line-height:12.5px;margin-top:14px;color:#333}
.band{position:absolute;top:942px;left:0;width:960px;height:174px;background:var(--brand);color:var(--white);text-align:center}
.band .tagline{font-size:15px;line-height:18px;margin-top:26px;font-weight:400}
.partner-row{position:absolute;top:100px;left:0;width:960px}
.partner{position:absolute;top:0;display:flex;align-items:center;gap:8px;font-size:24px;font-weight:300;white-space:nowrap}
.partner .dot{width:46px;height:46px;border-radius:50%;background:var(--white)}
.site-footer{position:absolute;top:1116px;left:0;width:960px;height:84px;background:var(--footer)}
.footer-brand{position:absolute;left:102px;top:34px;display:flex;align-items:center;gap:6px;color:#555}
.footer-brand .brand-mark{width:26px;height:26px;border:2px solid #555}
.footer-brand .brand-name{font-size:9px;line-height:9px}
.copyright{position:absolute;left:231px;top:48px;font-size:10px;color:#333}
.footer-nav{position:absolute;left:364px;top:48px;font-size:10px}
.footer-nav a{color:#333;text-decoration:none;margin-right:7px}
.social{position:absolute;left:738px;top:39px;display:flex;gap:8px}
.social span{width:22px;height:22px;border-radius:50%;background:#555}
</style>
</head>
<body>
<header class="site-header">
  <div class="brand"><div class="brand-mark"></div><div class="brand-name">Harbor<br>Ledger<br>Allies</div></div>
  <nav class="main-nav">
    <a href="#">Home</a><a href="#">Services</a><a href="#">Locations</a><a href="#">Partners</a><a href="#">FAQ</a><a href="#">Contact</a>
  </nav>
</header>

<div class="hero" role="img" aria-label="Photo of two professionals working at a desk with a calculator, pens and financial charts"></div>

<section class="why">
  <h1>Why Choose Our Services</h1>
  <p>Beciegast nveriti vitaesaert asety kertya aset aplica binerafae kertyu estyasnemo faserani ptaiades kertyaser daesraeds. Casrolern atur aut oditaut. Binsequuntur magni dolqui ratione volmsequi nesciu orbosas numquam eius modi eincidunt, ut labore et dolore magnam.</p>
  <a class="btn" href="#">read more</a>
</section>

<section class="services">
  <div class="service" style="left:106px">
    <div class="service-icon">
      <svg width="26" height="32" viewBox="0 0 26 32"><rect x="1" y="1" width="24" height="30" rx="2" fill="#fff"/><rect x="4" y="4" width="18" height="6" fill="#009ddd"/><g fill="#009ddd"><rect x="5" y="13" width="4" height="3"/><rect x="11" y="13" width="4" height="3"/><rect x="17" y="13" width="4" height="3"/><rect x="5" y="19" width="4" height="3"/><rect x="11" y="19" width="4" height="3"/><rect x="17" y="19" width="4" height="3"/><rect x="5" y="25" width="4" height="3"/><rect x="11" y="25" width="4" height="3"/><rect x="17" y="25" width="4" height="3"/></g></svg>
    </div>
    <h2>Accounting</h2>
    <p>Wolore sereledusempquibderumoms odes necessitatibus saepe eveniredums estu Etoluptates estudesu usandaeltaque earumul rerum hic tenetura sapientemi delecut mode.</p>
  </div>
  <div class="service" style="left:370px">
    <div class="service-icon">
      <svg width="36" height="30" viewBox="0 0 36 30"><g fill="#fff"><rect x="1" y="2" width="9" height="27" rx="1"/><rect x="12" y="2" width="9" height="27" rx="1"/><rect x="23" y="3" width="9" height="26" rx="1" transform="rotate(-12 27 16)"/></g><g fill="#009ddd"><rect x="3" y="6" width="5" height="8"/><rect x="14" y="6" width="5" height="8"/><circle cx="5.5" cy="23" r="1.6"/><circle cx="16.5" cy="23" r="1.6"/></g></svg>
    </div>
    <h2>Bookkeeping</h2>
    <p>Wolore sereledusempquibderumoms odes necessitatibus saepe eveniredums estu Etoluptates estudesu usandaeltaque earumul rerum hic tenetura sapientemi delecut mode.</p>
  </div>
  <div class="service" style="left:631px">
    <div class="service-icon">
      <svg width="30" height="30" viewBox="0 0 30 30"><rect x="2" y="4" width="26" height="24" rx="2" fill="#fff"/><rect x="2" y="4" width="26" height="6" fill="#fff"/><rect x="7" y="1" width="3" height="6" fill="#fff"/><rect x="20" y="1" width="3" height="6" fill="#fff"/><g fill="#009ddd"><rect x="5" y="12" width="5" height="4"/><rect x="12" y="12" width="5" height="4"/><rect x="19" y="12" width="5" height="4"/><rect x="5" y="18" width="5" height="4"/><rect x="12" y="18" width="5" height="4"/><rect x="19" y="18" width="5" height="4"/></g></svg>
    </div>
    <h2>Tax Planning</h2>
    <p>Wolore sereledusempquibderumoms odes necessitatibus saepe eveniredums estu Etoluptates estudesu usandaeltaque earumul rerum hic tenetura sapientemi delecut mode.</p>
  </div>
</section>

<section class="band">
  <p class="tagline">Experience and competency in complex numerical manipulations<br>Scrupulous accounting for your business.</p>
  <div class="partner-row">
    <div class="partner" style="left:106px"><span class="dot"></span>Tallymint Web</div>
    <div class="partner" style="left:383px">PennyTrim.example</div>
    <div class="partner" style="left:660px">Brightfolio.example</div>
  </div>
</section>

<footer class="site-footer">
  <div class="footer-brand"><div class="brand-mark"></div><div class="brand-name">Harbor<br>Ledger<br>Allies</div></div>
  <p class="copyright">© Copyright 2014</p>
  <nav class="footer-nav">
    <a href="#">Home</a><a href="#">Services</a><a href="#">Locations</a><a href="#">Partners</a><a href="#">FAQ</a><a href="#">Contact</a><a href="#">Privacy Policy</a><a href="#">Terms</a>
  </nav>
  <div class="social" aria-label="Social links"><span></span><span></span><span></span><span></span></div>
</footer>
</body>
</html>
```